Stationery Design Project

We are a packaging machinery manufacturer that mainly serve the food industry.
We now require a full set of stationary including name card, envelop, letter paper, and etc. to match our company image. The logo has been awarded in a previous contest which is attached here.
Updates
Project Deadline Extended
Reason: We have extended the deadline. We have adjusted the deadline before launch to avoid confusion but it turns out the new date wasn't implemented by the system. All designers please feel free to submit your design. Thank you!
Target Market(s)
B2B customer, including decision maker in food factories, chemical factories, etc.
Industry/Entity Type
Industry
Colors
Designer to choose colors to be used in the design.
Look and feel
Each slider illustrates characteristics of the customer's brand and the style your logo design should communicate.

```html
<!DOCTYPE html>
<html lang="en">
<head>
<meta charset="utf-8">
<title>Talvek Stationery Set</title>
<link rel="stylesheet" href="https://fonts.googleapis.com/css2?family=Arimo:wght@400;700&display=swap">
<style>
  :root {
    --backdrop: #45484c;
    --paper: #ffffff;
    --brand-green: #0f6b35;
    --accent-grey: #9a9c9f;
    --ink: #1b1b1b;
    --divider: #c9c9c9;
    --card-edge: #d4d4d4;
  }
  * { box-sizing: border-box; margin: 0; padding: 0; }
  html, body { width: 1164px; height: 1200px; overflow: hidden; }
  body {
    background: var(--backdrop);
    font-family: "Arimo", Arial, sans-serif;
    color: var(--ink);
    position: relative;
  }
  .sheet { position: absolute; background: var(--paper); }

  .brand {
    position: absolute;
    display: flex; align-items: center; gap: 6px;
    color: var(--brand-green);
    font-weight: 700; letter-spacing: 0.02em; line-height: 1;
  }
  .brand-square { background: var(--brand-green); display: inline-block; }
  .brand--white { color: var(--paper); }
  .brand--white .brand-square { background: var(--paper); }

  .contact-list { position: absolute; list-style: none; }
  .contact-list li { display: flex; align-items: center; white-space: nowrap; }
  .contact-list svg { fill: var(--brand-green); flex: none; }

  .band { position: absolute; left: 0; }
  .band svg { display: block; width: 100%; height: 100%; }
  .band-url {
    position: absolute; top: 0; bottom: 0;
    display: flex; align-items: center;
    color: var(--paper); white-space: nowrap;
  }

  /* Letter paper (rear) */
  .letter-rear { left: 533px; top: 231px; width: 576px; height: 816px; }
  .letter-rear .contact-list { left: 440px; top: 12px; font-size: 13.5px; }
  .letter-rear .contact-list li { height: 22px; gap: 7px; }
  .letter-rear .rule { position: absolute; left: 430px; top: 14px; width: 1px; height: 62px; background: var(--divider); }

  /* Letter paper (front) */
  .letter-front { left: 381px; top: 73px; width: 579px; height: 818px; }
  .letter-front .brand { left: 22px; top: 26px; font-size: 38px; }
  .letter-front .brand-square { width: 30px; height: 30px; }
  .sender { position: absolute; left: 326px; top: 22px; font-size: 14px; line-height: 17px; font-style: normal; }
  .sender strong { font-weight: 700; }
  .letter-front .contact-list { left: 448px; top: 14px; font-size: 13.5px; }
  .letter-front .contact-list li { height: 22px; gap: 7px; }
  .vrule { position: absolute; width: 1px; background: var(--divider); }

  /* Envelope */
  .envelope { left: 73px; top: 351px; width: 610px; height: 305px; }
  .envelope .brand { left: 20px; top: 23px; font-size: 32px; }
  .envelope .brand-square { width: 25px; height: 25px; }
  .return-address { position: absolute; left: 20px; top: 62px; font-size: 14px; line-height: 17px; font-style: normal; }

  /* Business card front */
  .card-front {
    left: 835px; top: 357px; width: 245px; height: 134px;
    border: 1px solid var(--card-edge);
    box-shadow: 2px 3px 5px rgba(0,0,0,0.22);
  }
  .card-front .brand { left: 7px; top: 7px; font-size: 25px; }
  .card-front .brand-square { width: 19px; height: 19px; }
  .holder { position: absolute; right: 5px; top: 7px; text-align: right; }
  .holder-name { font-size: 12px; }
  .holder-role { font-size: 8px; color: var(--brand-green); margin-top: 2px; }
  .card-front .contact-list { left: 172px; top: 79px; font-size: 8px; }
  .card-front .contact-list li { height: 12px; gap: 4px; }
  .card-address { position: absolute; left: 7px; top: 95px; font-size: 8px; line-height: 10px; font-style: normal; }

  /* Business card back */
  .card-back {
    left: 835px; top: 517px; width: 245px; height: 139px;
    box-shadow: 2px 3px 5px rgba(0,0,0,0.22);
  }
  .card-back .panel { position: absolute; left: 0; top: 0; width: 100%; height: 124px; background: var(--brand-green); }
  .card-back .brand { left: 40px; top: 46px; font-size: 36px; }
  .card-back .brand-square { width: 26px; height: 26px; }
  .card-back-url { position: absolute; left: 128px; top: 126px; font-size: 9px; }
  .card-back .tab { position: absolute; right: 0; top: 124px; width: 24px; height: 15px; }
</style>
</head>
<body>

<svg width="0" height="0" style="position:absolute" aria-hidden="true">
  <symbol id="icon-phone" viewBox="0 0 20 16">
    <path d="M2 6C2 2 18 2 18 6l-4 1-1-2H7L6 7 2 6z"/>
    <path d="M5 8h10l3 7H2l3-7zm5 1.5a2.3 2.3 0 1 0 0 4.6 2.3 2.3 0 0 0 0-4.6z"/>
  </symbol>
  <symbol id="icon-fax" viewBox="0 0 20 16">
    <rect x="5" y="0" width="10" height="6"/>
    <rect x="1" y="5" width="18" height="9" rx="1.5"/>
    <rect x="5" y="10" width="10" height="6" fill="#fff"/>
    <rect x="6" y="11" width="8" height="4"/>
  </symbol>
  <symbol id="icon-mail" viewBox="0 0 20 14">
    <rect x="0" y="0" width="20" height="14" rx="1"/>
    <path d="M2 2l8 6 8-6" fill="none" stroke="#fff" stroke-width="1.6"/>
  </symbol>
</svg>

<!-- Rear letter paper -->
<section class="sheet letter-rear">
  <span class="rule"></span>
  <ul class="contact-list">
    <li><svg width="18" height="14"><use href="#icon-phone"/></svg>800.555.0142</li>
    <li><svg width="18" height="14"><use href="#icon-fax"/></svg>800.555.0142</li>
    <li><svg width="18" height="13"><use href="#icon-mail"/></svg>info@talvek.com</li>
  </ul>
  <div class="band" style="top:780px;width:576px;height:20px;">
    <svg viewBox="0 0 576 20" preserveAspectRatio="none">
      <polygon points="0,0 524,0 516,10 524,20 0,20" fill="var(--brand-green)"/>
      <polygon points="536,0 576,0 576,20 536,20 528,10" fill="var(--accent-grey)"/>
    </svg>
    <span class="band-url" style="right:70px;font-size:13px;">www.talvek.com</span>
  </div>
</section>

<!-- Front letter paper -->
<section class="sheet letter-front">
  <div class="brand"><span class="brand-square"></span>TALVEK</div>
  <address class="sender">
    <strong>TALVEK</strong><br>218 Mill Road<br>Lodi, CA 95240
  </address>
  <span class="vrule" style="left:436px;top:18px;height:56px;"></span>
  <ul class="contact-list">
    <li><svg width="18" height="14"><use href="#icon-phone"/></svg>800.555.0142</li>
    <li><svg width="18" height="14"><use href="#icon-fax"/></svg>800.555.0142</li>
    <li><svg width="18" height="13"><use href="#icon-mail"/></svg>info@talvek.com</li>
  </ul>
  <div class="band" style="top:772px;width:579px;height:19px;">
    <svg viewBox="0 0 579 19" preserveAspectRatio="none">
      <polygon points="0,0 536,0 528,9.5 536,19 0,19" fill="var(--brand-green)"/>
      <polygon points="546,0 579,0 579,19 546,19 538,9.5" fill="var(--accent-grey)"/>
    </svg>
    <span class="band-url" style="right:70px;font-size:13px;">www.talvek.com</span>
  </div>
</section>

<!-- Envelope -->
<section class="sheet envelope">
  <div class="brand"><span class="brand-square"></span>TALVEK</div>
  <address class="return-address">218 Mill Road<br>Lodi, CA 95240</address>
  <div class="band" style="top:273px;width:610px;height:20px;">
    <svg viewBox="0 0 610 20" preserveAspectRatio="none">
      <polygon points="0,0 572,0 564,10 572,20 0,20" fill="var(--brand-green)"/>
      <polygon points="582,0 610,0 610,20 582,20 574,10" fill="var(--accent-grey)"/>
    </svg>
    <span class="band-url" style="right:64px;font-size:13px;">www.talvek.com</span>
  </div>
</section>

<!-- Business card, front -->
<section class="sheet card-front">
  <div class="brand"><span class="brand-square"></span>TALVEK</div>
  <div class="holder">
    <p class="holder-name">Daniel Reyes</p>
    <p class="holder-role">President &amp; CEO</p>
  </div>
  <address class="card-address">218 Mill Road<br>Lodi, CA 95240</address>
  <ul class="contact-list">
    <li><svg width="10" height="8"><use href="#icon-phone"/></svg>800.555.0142</li>
    <li><svg width="10" height="8"><use href="#icon-fax"/></svg>800.555.0142</li>
    <li><svg width="10" height="7"><use href="#icon-mail"/></svg>info@talvek.com</li>
  </ul>
  <div class="band" style="top:118px;width:243px;height:12px;">
    <svg viewBox="0 0 243 12" preserveAspectRatio="none">
      <polygon points="0,0 216,0 210,6 216,12 0,12" fill="var(--brand-green)"/>
      <polygon points="223,0 243,0 243,12 223,12 217,6" fill="var(--accent-grey)"/>
    </svg>
    <span class="band-url" style="left:117px;font-size:8px;">company slogan</span>
  </div>
</section>

<!-- Business card, back -->
<section class="sheet card-back">
  <div class="panel"></div>
  <div class="brand brand--white"><span class="brand-square"></span>TALVEK</div>
  <span class="card-back-url">www.talvek.com</span>
  <svg class="tab" viewBox="0 0 24 15" aria-hidden="true">
    <polygon points="6,0 24,0 24,15 6,15 0,7.5" fill="var(--accent-grey)"/>
  </svg>
</section>

</body>
</html>
```